Wedding Startup Full Website Design

We've just completed our online platform and need to create a website that represents our brand and vision, and clearly communicates our features and value proposition to potential users. There are a minimum of 4 pages that need to be designed. One geared toward wedding professionals (venues/vendors/coordinators), another toward engaged couples, one showcasing features, and an 'About Us' page.

The designer will creative freedom to create a unique UI/UX as long as it represents our brand and is relevant to our target audience/market. The ideal candidate will be able to assume the mindset of someone working in the wedding industry and/or an engaged couple. Ability to create illustrations is a plus.

Copy will be provided as needed. We will reimburse for stock images (pending approval before purchasing), but sourcing the stock images will be the responsibility of the designer.

Our current website: https://www.trelmora.com
Updates

Our project has now been guaranteed! We look forward to finding the perfect design for our site pages!

Still waiting for a design that stands out from the rest and aligns with the creative brief.

Target Market(s)

Wedding Professionals and Engaged Couples

Industry/Entity Type

Wedding

Number of Pages Required

4 page

Font styles to use
Sans Serif

Colors
ffffff
fbd4d5
f59195
33a6d7
cadf82
86cfc6

Requirements
Must have
• Common sense stuff like having a unified brand that accurately represents our platform, speaks to our target market, and clearly articulates our vision
Nice to have
• Illustrations
Should not have
• Overly cheesy or childish. We want to be professional but still embrace the wedding culture.

```html
<!DOCTYPE html>
<html lang="en">
<head>
<meta charset="utf-8">
<title>Trelmora – About Us</title>
<link rel="stylesheet" href="https://fonts.googleapis.com/css2?family=Raleway:ital,wght@0,300;0,400;0,500;0,600;0,800;1,800&display=swap">
<style>
  :root {
    --white: #ffffff;
    --blush: #fbd4d5;
    --coral: #f59195;
    --sky: #33a6d7;
    --lime: #cadf82;
    --mint: #86cfc6;
    --ink: #2b2b2b;
    --muted: #6f6f6f;
    --page: #f8f8f8;
    --band: #f5f3ee;
    --rule: #e2e2e2;
  }
  * { box-sizing: border-box; margin: 0; padding: 0; }
  html, body { width: 1200px; height: 2200px; overflow: hidden; }
  body {
    position: relative;
    background: var(--page);
    font-family: "Raleway", sans-serif;
    color: var(--ink);
  }
  .abs { position: absolute; }

  /* Header */
  .site-header {
    position: absolute; left: 0; top: 0; width: 1200px; height: 100px;
    background: var(--white); border-bottom: 2px solid #dcdcdc;
  }
  .brand {
    position: absolute; display: flex; align-items: center; gap: 10px;
    font-family: "Raleway", sans-serif; font-weight: 500; color: var(--sky);
  }
  .brand-mark { border: 3px solid var(--coral); }
  .site-header .brand { left: 129px; top: 26px; font-size: 40px; }
  .site-header .brand-mark { width: 26px; height: 26px; }
  .main-nav { position: absolute; top: 43px; left: 406px; display: flex; gap: 0; font-size: 11.5px; font-weight: 500; }
  .main-nav a { position: absolute; white-space: nowrap; text-decoration: none; color: var(--ink); }
  .main-nav .is-pro { color: var(--coral); }
  .main-nav .is-active { color: var(--sky); }
  .demo-button {
    position: absolute; left: 929px; top: 25px; width: 149px; height: 48px;
    background: var(--coral); color: var(--white); border-radius: 3px;
    font-size: 9px; font-weight: 600; letter-spacing: .3px;
    display: flex; align-items: center; justify-content: center;
  }

  /* Section titles */
  .section-title {
    position: absolute; left: 0; width: 1200px; text-align: center;
    font-size: 23px; font-weight: 600; color: var(--ink);
  }
  .ornament {
    position: absolute; left: 496px; width: 208px; height: 12px;
    background: linear-gradient(90deg, transparent, var(--blush) 15%, var(--coral) 50%, var(--blush) 85%, transparent);
    border-radius: 6px; opacity: .8;
  }

  /* Value cards */
  .value-card {
    position: absolute; top: 239px; width: 300px; height: 600px; overflow: hidden;
    color: var(--white); font-weight: 300; font-size: 35px; line-height: 40px;
  }
  .value-card p { position: absolute; left: 33px; right: 20px; }
  .value-card em { font-style: italic; font-weight: 800; color: var(--lime); }
  .card-inspire { left: 120px; border-top-left-radius: 90px;
    background: linear-gradient(160deg, #4d5a6c 0%, #7d8796 45%, #a8a8aa 100%); }
  .card-enjoy { left: 450px;
    background: linear-gradient(170deg, #5f7c4c 0%, #a9a293 40%, #c9bfb2 100%); }
  .card-growth { left: 779px; width: 301px; border-top-right-radius: 90px;
    background: linear-gradient(165deg, #5b4130 0%, #3a2a22 55%, #2a1d17 100%); }

  /* Mission */
  .mission {
    position: absolute; left: 120px; top: 839px; width: 960px; height: 367px;
    background: #f3f3f3; overflow: hidden;
  }
  .mission-flowers {
    position: absolute; left: 0; bottom: 0; width: 960px; height: 130px;
    background: linear-gradient(180deg, rgba(243,243,243,0) 0%, #e6e9d8 45%, #efe1dc 100%);
  }
  .mission-text {
    position: absolute; left: 90px; width: 780px; text-align: center;
    font-size: 11.5px; line-height: 21px; color: #555;
  }

  /* Advisory */
  .advisory-band { position: absolute; left: 0; top: 1206px; width: 1200px; height: 661px; background: var(--band); }
  .member {
    position: absolute; top: 1405px; width: 300px; height: 399px; background: var(--white);
  }
  .member.is-featured { box-shadow: 0 2px 6px rgba(0,0,0,.18); height: 401px; }
  .member-photo { position: absolute; left: 0; top: 0; width: 100%; height: 300px;
    background: linear-gradient(180deg, #d5d9de 0%, #9fb7cf 100%); }
  .is-featured .member-photo { height: 250px; background: linear-gradient(180deg, #8a9aa8 0%, #2f3d55 100%); }
  .member-name { position: absolute; left: 20px; font-size: 17px; color: var(--coral); }
  .member-role { position: absolute; left: 20px; font-size: 12.5px; color: var(--muted); }
  .member-social { position: absolute; left: 20px; top: 361px; display: flex; gap: 13px; }
  .member-social span { width: 11px; height: 11px; border-radius: 50%; background: #555; }
  .member-social span.is-hover { background: var(--coral); }

  /* Footer */
  .site-footer .brand { left: 0; width: 1200px; justify-content: center; top: 1918px; font-size: 48px; }
  .site-footer .brand-mark { width: 30px; height: 30px; }
  .social-links { position: absolute; top: 2035px; left: 524px; display: flex; gap: 8px; }
  .social-links span { width: 32px; height: 32px; border-radius: 50%; background: var(--coral); }
  .social-links span.is-hover { background: var(--white); border: 2px solid var(--coral); }
  .footer-rule { position: absolute; left: 0; top: 2120px; width: 1200px; height: 2px; background: var(--rule); }
  .copyright { position: absolute; left: 150px; top: 2155px; font-size: 11px; color: var(--muted); }
  .back-to-top {
    position: absolute; left: 1060px; top: 2107px; width: 50px; height: 50px; background: var(--coral);
    display: flex; align-items: center; justify-content: center;
  }
</style>
</head>
<body>

<header class="site-header">
  <div class="brand"><span class="brand-mark"></span>Trelmora</div>
  <nav class="main-nav">
    <a href="#" style="left:0">ABOUT US</a>
    <a href="#" class="is-pro" style="left:90px">PROFESSIONALS</a>
    <a href="#" class="is-active" style="left:216px">FEATURES</a>
    <a href="#" style="left:305px">FOR COUPLES</a>
  </nav>
  <a class="demo-button">ACCESS DEMO</a>
</header>

<h2 class="section-title" style="top:136px">About Us</h2>
<div class="ornament" role="img" aria-label="Pink floral divider ornament" style="top:180px"></div>

<section class="value-card card-inspire" role="img" aria-label="Photo of a couple embracing at their wedding">
  <p style="top:92px"><em>Inspire</em> innovation and bringing dream weddings to life.</p>
</section>
<section class="value-card card-enjoy" role="img" aria-label="Photo of a bride with a wedding planner at a table setting">
  <p style="top:157px">For wedding professions and couples to <em>enjoy</em> the wedding planning experience.</p>
</section>
<section class="value-card card-growth" role="img" aria-label="Photo of a laptop on a wooden desk">
  <p style="top:340px">Foster <em>growth</em> for our partners and within the wedding industry.</p>
</section>

<section class="mission">
  <div class="mission-flowers" role="img" aria-label="Soft pastel roses and hellebore flowers along the bottom edge"></div>
  <h2 class="section-title" style="left:-120px;top:60px">Mission Statement</h2>
  <div class="ornament" role="img" aria-label="Pink floral divider ornament" style="left:376px;top:104px"></div>
  <p class="mission-text" style="top:150px">Weddings are one the most memorable events in people's life. Unfortunately planning a wedding is filled with stress, often leaving wedding professionals and their clients with soured memories.</p>
  <p class="mission-text" style="top:213px">Our vision at Trelmora is to revamp the way weddings are planned on both sides of the process (wedding professionals and their clients). We aim to reduce the stress of everyone involved, and make the engagement season and wedding day memorable for the right reasons.</p>
</section>

<div class="advisory-band"></div>
<h2 class="section-title" style="top:1304px">Advisory Board</h2>
<div class="ornament" role="img" aria-label="Pink floral divider ornament" style="top:1354px"></div>

<article class="member" style="left:120px">
  <div class="member-photo" role="img" aria-label="Portrait photo of Marcus Dalby"></div>
  <div class="member-name" style="top:323px">Marcus Dalby</div>
  <div class="member-role" style="top:358px">Technical</div>
</article>
<article class="member is-featured" style="left:449px">
  <div class="member-photo" role="img" aria-label="Portrait photo of Jonah Whitfield"></div>
  <div class="member-name" style="top:273px">Jonah Whitfield</div>
  <div class="member-role" style="top:308px">Operations</div>
  <div class="member-social"><span></span><span class="is-hover"></span><span></span><span></span><span></span><span></span></div>
</article>
<article class="member" style="left:776px">
  <div class="member-photo" role="img" aria-label="Portrait photo of Peter Ansell"></div>
  <div class="member-name" style="top:323px">Peter Ansell</div>
  <div class="member-role" style="top:358px">Marketing</div>
</article>

<footer class="site-footer">
  <div class="brand"><span class="brand-mark"></span>Trelmora</div>
  <div class="social-links"><span class="is-hover"></span><span></span><span></span><span></span></div>
  <div class="footer-rule"></div>
  <p class="copyright">Trelmora ©2018 All Rights Reserved</p>
  <a class="back-to-top" aria-label="Back to top">
    <svg width="20" height="12" viewBox="0 0 20 12"><path d="M2 10 L10 2 L18 10" fill="none" stroke="#fff" stroke-width="2.5"/></svg>
  </a>
</footer>

</body>
</html>
```